Simple and clean webdesign for personal homepage

Trying to create a simple and clean webdesign for my personal homepage. Going to use a static site builder with templates to build the site. I want it to have multiple pages - like an about me, blog and resume. I just need something very basic I can customize. I want the main colors to be purple, black and white. I am open to other color palettes too but since purple is my favorite color I want that to be one of the main colors.

The site be mostly text driven. Might have some images in the body text but I want the site design to be light and lean.

Industry/Entity Type

Personal Homepage.

Coding

Coded - Design and coding required

Number of Pages Required

1 page

Font styles to use
Sans Serif

Colors
6B429C
8869AF
B7A5CE
E3DAEB
F3F0F8

Requirements
Must have
• Clean design. Purple used as a color. HTML template.
Nice to have
• Responsive

```html
<!DOCTYPE html>
<html lang="en">
<head>
<meta charset="UTF-8">
<title>Henrik Aldmar</title>
<link href="https://fonts.googleapis.com/css2?family=Poppins:wght@500&family=Work+Sans:wght@400;500;600&display=swap" rel="stylesheet">
<style>
:root{
  --purple:#6b429c;
  --ink:#2f2f33;
  --header-bg:#f3f3f3;
  --field-bg:rgba(240,241,244,0.88);
  --hero-top:#dcdee4;
  --hero-mid:#c9ccd6;
  --hero-low:#bfc3d0;
  --photo-top:#cfd1d8;
  --photo-mid:#6f84a6;
  --photo-low:#2c3447;
}
*{margin:0;padding:0;box-sizing:border-box}
html,body{width:1200px;height:573px;overflow:hidden}
body{position:relative;font-family:"Work Sans",Arial,sans-serif;color:var(--ink);background:var(--hero-mid)}
.site-header{position:absolute;left:0;top:0;width:1200px;height:76px;background:var(--header-bg);border-bottom:1px solid #d8d8d8}
.brand{position:absolute;left:141px;top:14px;font-family:"Poppins",Arial,sans-serif;font-weight:500;font-size:38px;line-height:1.2;color:var(--purple)}
.main-nav{position:absolute;left:599px;top:34px;display:flex;gap:22px;font-size:13.5px;font-weight:400;color:var(--ink)}
.main-nav a{color:inherit;text-decoration:none}
.nav-divider{position:absolute;left:909px;top:24px;width:1px;height:37px;background:#c4c4c4}
.header-phone{position:absolute;left:924px;top:31px;display:flex;align-items:center;gap:8px;font-size:13.5px;font-weight:400}
.hero-backdrop{position:absolute;left:0;top:76px;width:1200px;height:497px;background:linear-gradient(180deg,var(--hero-top) 0%,var(--hero-mid) 55%,var(--hero-low) 100%)}
.portrait-photo{position:absolute;left:0;top:76px;width:372px;height:497px;background:linear-gradient(180deg,var(--photo-top) 0%,var(--photo-mid) 60%,var(--photo-low) 100%);opacity:.8}
.intro{position:absolute;left:448px;top:141px;width:612px}
.intro h1{font-size:24px;font-weight:600;color:var(--purple);margin-bottom:10px}
.intro p{font-size:12px;line-height:20.5px;letter-spacing:.15px;margin-bottom:2px}
.quick-contact{position:absolute;left:448px;top:320px;width:580px}
.quick-contact h2{font-size:25px;font-weight:400;margin-bottom:12px;letter-spacing:.3px}
.field-row{display:flex;gap:10px;margin-bottom:5px}
.field{height:39px;background:var(--field-bg);font-size:10.5px;padding:13px 7px;color:var(--ink)}
.field.short{width:187px}
.field.message{width:455px}
.submit{width:118px;height:39px;background:var(--purple);color:#fff;font-size:17px;font-weight:500;display:flex;align-items:center;justify-content:center}
.site-footer{position:absolute;left:448px;top:526px;font-size:12px;letter-spacing:.2px}
</style>
</head>
<body>
<header class="site-header">
  <div class="brand">Henrik Aldmar</div>
  <nav class="main-nav"><a href="#">About Me</a><a href="#">Blog</a><a href="#">Resume</a><a href="#">Contact Me</a></nav>
  <div class="nav-divider"></div>
  <div class="header-phone">
    <svg width="22" height="22" viewBox="0 0 24 24" fill="none" stroke="#333" stroke-width="1.5" stroke-linecap="round" stroke-linejoin="round"><path d="M6 3l3 4-2 2c1 3 4 6 7 7l2-2 4 3-2 3C10 20 4 14 3 5z"/><path d="M14 6a5 5 0 0 1 4 4"/><path d="M14 2a9 9 0 0 1 8 8"/></svg>
    <span>555.014.2286</span>
  </div>
</header>

<div class="hero-backdrop" role="img" aria-label="Soft background photo of snowy hills and bare winter trees"></div>
<div class="portrait-photo" role="img" aria-label="Portrait photo of the site owner in a dark blazer and blue shirt"></div>

<section class="intro">
  <h1>Henrik Aldmar</h1>
  <p>Lorem ipsum dolor sit amet, consecte ipiscing elit, sed diam nonummy nibh euismod tincidunt ut laoreet dolore magna aliqnibh euismod tincidunt ut laoreet dolore magna aliquam erat volutpat. Ut wisi enim ad minim veniam, quis.</p>
  <p>Lorem ipsum dolor sit amet, consecte ipiscing elit, sed diam nonummy nibh euismod tincidunt ut laoreet dolore magna aliqnibh euismod tincidunt ut laoreet</p>
</section>

<section class="quick-contact">
  <h2>Quick Contact</h2>
  <div class="field-row">
    <div class="field short">Name</div>
    <div class="field short">Phone</div>
    <div class="field short">Email Address</div>
  </div>
  <div class="field-row">
    <div class="field message">Message</div>
    <div class="submit">Submit</div>
  </div>
</section>

<footer class="site-footer">© 2022 Henrik Aldmar&nbsp; All Right Reserved.</footer>
</body>
</html>
```